Web Design

QLV Institute offers a one stop solution for people to be introduced to the world of Forex trading. We have interactive forex room, one on one coaching by our experienced trading experts.
Main menus:
1. Learn to trade
2. About us
3. Brokers
4. Money management and risk
5. FAQ
6. Register – scroll down menu with registration form (name, email and register button)
7. Contact us
The webpage should have:
1. Large text style and images
2. Join / Get Started Buttons
3. Instructors profile
4. People Testimonies
5. Recommended Brokers
6. Live rates
7. Live support
8. Social icons: facebook, twitter and g+

Project Deadline Extended
Reason: I just added a logo on the attachment

Industry/Entity Type

Trade

```html
<!DOCTYPE html>
<html lang="en">
<head>
<meta charset="utf-8">
<title>QLV Institute</title>
<link href="https://fonts.googleapis.com/css2?family=Oswald:wght@400;500&family=Open+Sans:ital,wght@0,400;0,600;0,700;1,400&display=swap" rel="stylesheet">
<style>
:root{
  --navy:#0c2c4a;
  --navy-dark:#072039;
  --green:#6db52f;
  --green-dark:#3f8a17;
  --green-light:#9ad23f;
  --ink:#222;
  --grey:#555;
  --light:#f1f2f4;
  --band:#363636;
  --white:#fff;
}
*{margin:0;padding:0;box-sizing:border-box}
html,body{width:1200px;height:2380px;overflow:hidden;background:var(--white)}
body{font-family:"Open Sans",Arial,sans-serif;color:var(--ink);position:relative}
.abs{position:absolute}
.oswald{font-family:"Oswald",Arial,sans-serif}

/* header */
.header{position:absolute;left:0;top:0;width:1200px;height:120px;background:var(--white)}
.header-dark{position:absolute;left:0;top:0;width:1200px;height:120px}
.brand{position:absolute;left:160px;top:38px;display:flex;align-items:center;gap:12px;font-family:"Open Sans",sans-serif;font-weight:700;font-size:30px;color:var(--navy)}
.brand-dot{width:22px;height:22px;background:var(--green)}
.call{position:absolute;left:506px;top:44px;color:var(--green);font-size:17px}
.call strong{display:block;color:var(--white);font-size:30px;font-weight:600;line-height:36px}
.social-top{position:absolute;left:976px;top:0;display:flex;gap:6px}
.social-top span{width:28px;height:28px;background:var(--green)}
.live-btn{position:absolute;left:905px;top:52px;width:170px;height:42px;background:var(--white);border-radius:6px;display:flex;align-items:center;gap:10px;padding-left:8px;font-weight:700;font-size:15px;color:var(--ink)}
.live-btn i{width:30px;height:30px;border-radius:50%;border:3px solid var(--ink)}

/* nav */
.nav{position:absolute;left:0;top:120px;width:1200px;height:55px;background:linear-gradient(#6fbb2a,#3e8f14)}
.nav a{position:absolute;top:0;height:55px;line-height:55px;color:var(--white);font-size:16px;text-decoration:none;text-align:center}
.nav a.active{background:var(--navy)}
.nav .sep{position:absolute;top:10px;width:1px;height:35px;background:rgba(255,255,255,.3)}

/* hero */
.hero{position:absolute;left:0;top:175px;width:1200px;height:325px;background:var(--white);border-bottom:5px solid var(--green)}
.hero-art{position:absolute;left:0;top:0;width:560px;height:320px;background:linear-gradient(120deg,#eef2f6 0%,#7fb2e3 45%,#1f4d86 75%,#f3a64a 100%)}
.hero h1{position:absolute;left:565px;top:66px;font-family:"Oswald",sans-serif;font-weight:400;font-size:48px;color:#111}
.hero p{position:absolute;left:572px;top:136px;font-family:"Oswald",sans-serif;font-size:23px;line-height:34px;color:#111}
.btn-green{position:absolute;background:linear-gradient(#7fcc34,#3f8a17);color:var(--white);font-family:"Oswald",sans-serif;font-size:21px;text-align:center;border-radius:3px}

/* welcome */
.welcome{position:absolute;left:0;top:505px;width:1200px;height:181px;background:var(--navy);text-align:center;color:var(--white)}
.welcome h2{font-family:"Oswald",sans-serif;font-weight:400;font-size:29px;margin-top:25px}
.welcome h2 span{color:var(--green-light)}
.welcome p{font-size:13px;line-height:25px;width:760px;margin:12px auto 0}
.notch{position:absolute;width:0;height:0;border-left:13px solid transparent;border-right:13px solid transparent}

/* rates */
.section-title{position:absolute;width:1200px;text-align:center;font-family:"Oswald",sans-serif;font-size:30px;color:#111}
.rate{position:absolute;width:300px;height:72px;border-bottom:2px solid #222}
.rate .name{position:absolute;left:0;top:6px;font-size:14px;line-height:19px;color:#222}
.rate .val{position:absolute;left:190px;top:10px;width:110px;height:30px;background:#222;color:var(--white);font-size:14px;text-align:center;line-height:30px;border-radius:2px}
.arrow-c{position:absolute;width:52px;height:52px;border-radius:50%;background:var(--white);box-shadow:0 0 6px rgba(0,0,0,.2)}

/* instructors */
.instructors{position:absolute;left:0;top:1097px;width:1200px;height:371px;background:radial-gradient(ellipse at center,#9cd43c 0%,#6aaa20 60%,#4f8c17 100%)}
.ins-title{position:absolute;left:0;top:36px;width:1200px;text-align:center;font-family:"Oswald",sans-serif;font-size:26px;color:#111}
.ins-line{position:absolute;top:55px;width:110px;height:2px;background:rgba(255,255,255,.6)}
.profile{position:absolute;width:200px;text-align:center}
.profile .photo{width:146px;height:146px;margin:0 auto;border-radius:50%;border:8px solid var(--navy);background:linear-gradient(#e6e6e6,#b5a08a)}
.profile .pin{width:0;height:0;margin:-6px auto 0;border-left:14px solid transparent;border-right:14px solid transparent;border-top:14px solid var(--navy)}
.profile h3{font-family:"Oswald",sans-serif;font-weight:400;font-size:28px;color:#111;margin-top:6px}
.profile a{display:inline-block;margin-top:8px;width:82px;height:28px;line-height:28px;background:var(--navy);color:var(--white);font-size:12px;font-weight:700;text-decoration:none}
.side-tab{position:absolute;width:36px;height:56px;background:#e8e8e8;border-radius:6px}

/* live support */
.support{position:absolute;left:0;top:1468px;width:1200px;height:93px;background:var(--band)}
.support h2{position:absolute;left:327px;top:18px;font-family:"Oswald",sans-serif;font-weight:500;font-size:40px;color:var(--white);letter-spacing:1px}
.support h2 span{color:#8ab842}
.support .photo{position:absolute;left:738px;top:-20px;width:134px;height:134px;border-radius:50%;border:4px solid var(--white);background:linear-gradient(#f5f5f5,#c9a88c)}

/* brokers */
.brokers{position:absolute;left:0;top:1561px;width:1200px;height:260px;background:linear-gradient(100deg,#f7f8fa 0%,#dfe3e8 60%,#f0f2f4 100%)}
.brokers .photo{position:absolute;left:160px;top:14px;width:235px;height:246px;background:linear-gradient(#e7d8c8,#1d1d22)}
.brokers h2{position:absolute;left:437px;top:42px;font-family:"Oswald",sans-serif;font-weight:500;font-size:30px;color:#111}
.brokers p{position:absolute;left:437px;top:96px;width:625px;font-size:19px;line-height:33px;color:#222}
.btn-navy{position:absolute;background:var(--navy);color:var(--white);font-weight:600;font-size:16px;text-align:center;border-radius:4px}

/* testimonials */
.quote{position:absolute;left:140px;top:1963px;width:800px;height:108px;background:#ececec;border-radius:4px}
.quote p{padding:16px 24px 0 40px;font-style:italic;font-size:12.5px;line-height:23px;color:#444}
.quote-photo{position:absolute;left:940px;top:1958px;width:120px;height:120px;border-radius:50%;border:4px solid #fff;box-shadow:0 0 4px rgba(0,0,0,.3);background:linear-gradient(#dbe3ea,#9fb0c0)}

/* footer */
.footer{position:absolute;left:0;top:2146px;width:1200px;height:194px;background:var(--navy);color:var(--white)}
.footer h4{position:absolute;top:18px;font-weight:400;font-size:18px}
.footer ul{position:absolute;list-style:none;font-size:13px;line-height:24px}
.footer ul li::before{content:"› ";}
.footer .txt{position:absolute;font-size:13px;line-height:18px}
.footer .email-in{position:absolute;left:652px;top:100px;width:208px;height:26px;background:var(--white);color:#999;font-size:11px;line-height:26px;padding-left:8px}
.footer .sub{position:absolute;left:652px;top:140px;width:104px;height:28px;background:var(--green-dark);font-weight:700;font-size:13px;line-height:28px;text-align:center}
.footer .soc{position:absolute;top:64px;width:30px;height:30px;border-radius:50%;background:#d8d8d8}
.foot-brand{position:absolute;left:912px;top:120px;font-weight:700;font-size:28px;color:#21476d}
.copyright{position:absolute;left:0;top:2340px;width:1200px;height:40px;background:var(--navy-dark);color:var(--white);font-size:13px;text-align:center;line-height:40px}
</style>
</head>
<body>

<!-- header -->
<header class="header">
  <svg class="header-dark" width="1200" height="120" viewBox="0 0 1200 120" aria-hidden="true">
    <polygon points="370,0 1200,0 1200,120 455,120 395,60" fill="#0c2c4a"/>
  </svg>
  <div class="brand"><span class="brand-dot"></span>QLV Institute</div>
  <div class="call">Call Us Now<strong>555-010-2040</strong></div>
  <div class="social-top"><span></span><span></span><span></span></div>
  <div class="live-btn"><i></i>LIVE SUPPORT</div>
</header>

<!-- nav -->
<nav class="nav">
  <a class="active" style="left:132px;width:154px">Learn To Trade</a>
  <a style="left:300px;width:135px">About Us</a>
  <span class="sep" style="left:435px"></span>
  <a style="left:435px;width:130px">Brokers</a>
  <span class="sep" style="left:565px"></span>
  <a style="left:565px;width:265px">Money Management &amp; Risk</a>
  <span class="sep" style="left:830px"></span>
  <a style="left:830px;width:125px">FAQ's</a>
  <span class="sep" style="left:955px"></span>
  <a style="left:955px;width:140px">Contact Us</a>
  <span class="sep" style="left:1095px"></span>
</nav>

<!-- hero -->
<section class="hero">
  <div class="hero-art" role="img" aria-label="3D blue bar chart with a rising orange arrow on a grid"></div>
  <h1>We Are Ultimate Instructers</h1>
  <p>We Have Interactive Forex Room, One On One Coaching<br>By Our Experienced Trading Experts !</p>
  <a class="btn-green" style="left:573px;top:218px;width:205px;height:44px;line-height:44px">Get Started With Us</a>
</section>

<!-- welcome -->
<section class="welcome">
  <span class="notch" style="left:587px;top:-1px;border-top:13px solid #6db52f"></span>
  <h2>Welcome to <span>QLV INSTITUTE</span></h2>
  <p>Lorem ipsum dolor sit amet, consectetuer adipiscing elit, sed diam nonummy nibh euincidunt ut laoreet dolore magna aliqua. Ut wisi enim ad minim veniam, quis nostrud exerci tation ullamcorper suscipit lobortis nisl ut aliquip ex ea commodo consequat. Duis autem vel eum iriure dolor in hendrerit in vulputate velit .</p>
  <span class="notch" style="left:587px;top:181px;border-top:13px solid #0c2c4a"></span>
</section>

<!-- live rates -->
<h2 class="section-title" style="top:718px;font-weight:500">Live Rates</h2>
<div class="arrow-c" style="left:180px;top:898px"><svg width="52" height="52"><path d="M29 18 L21 26 L29 34" stroke="#111" stroke-width="3" fill="none"/></svg></div>
<div class="arrow-c" style="left:968px;top:898px"><svg width="52" height="52"><path d="M23 18 L31 26 L23 34" stroke="#111" stroke-width="3" fill="none"/></svg></div>

<div class="rate" style="left:275px;top:790px"><div class="name">Nordlane (NRDL)<br>10/3 - 10/3</div><div class="val">+$1.700</div></div>
<div class="rate" style="left:275px;top:862px"><div class="name">Nordlane (NRDL)<br>10/3 - 10/3</div><div class="val">+$1.700</div></div>
<div class="rate" style="left:275px;top:934px"><div class="name">Nordlane (NRDL)<br>10/3 - 10/3</div><div class="val">+$1.700</div></div>
<div class="rate" style="left:275px;top:1006px;border-bottom:none"><div class="name">Nordlane (NRDL)<br>10/3 - 10/3</div><div class="val">+$1.700</div></div>
<div class="rate" style="left:617px;top:790px"><div class="name">Harbor Metrics (HBMX)<br>9/18 - 9/23</div><div class="val">+$6.800</div></div>
<div class="rate" style="left:617px;top:862px"><div class="name">Harbor Metrics (HBMX)<br>9/18 - 9/23</div><div class="val">+$6.800</div></div>
<div class="rate" style="left:617px;top:934px"><div class="name">Harbor Metrics (HBMX)<br>9/18 - 9/23</div><div class="val">+$6.800</div></div>
<div class="rate" style="left:617px;top:1006px;border-bottom:none"><div class="name">Harbor Metrics (HBMX)<br>9/18 - 9/23</div><div class="val">+$6.800</div></div>

<!-- instructors -->
<section class="instructors">
  <span class="notch" style="left:587px;top:-1px;border-top:13px solid #fff"></span>
  <span class="ins-line" style="left:355px"></span>
  <div class="ins-title">INSTRUCTORS PROFILE</div>
  <span class="ins-line" style="left:735px"></span>
  <div class="side-tab" style="left:112px;top:160px"><svg width="36" height="56"><path d="M22 20 L14 28 L22 36 Z" fill="#222"/></svg></div>
  <div class="side-tab" style="left:1052px;top:160px"><svg width="36" height="56"><path d="M14 20 L22 28 L14 36 Z" fill="#222"/></svg></div>

  <div class="profile" style="left:165px;top:106px"><div class="photo" role="img" aria-label="Portrait of instructor Mark Holt"></div><div class="pin"></div><h3>Mark Holt</h3><a>Read More</a></div>
  <div class="profile" style="left:390px;top:106px"><div class="photo" role="img" aria-label="Portrait of instructor Owen Barker"></div><div class="pin"></div><h3>Owen Barker</h3><a>Read More</a></div>
  <div class="profile" style="left:623px;top:106px"><div class="photo" role="img" aria-label="Portrait of instructor Lena Varga"></div><div class="pin"></div><h3>Lena Varga</h3><a>Read More</a></div>
  <div class="profile" style="left:825px;top:106px"><div class="photo" role="img" aria-label="Portrait of instructor Peter Colby"></div><div class="pin"></div><h3>Peter Colby</h3><a>Read More</a></div>
</section>

<!-- live support -->
<section class="support">
  <h2>24/7 LIVE <span>SUPPORT</span></h2>
  <div class="photo" role="img" aria-label="Smiling support agents with headsets"></div>
</section>

<!-- recommended brokers -->
<section class="brokers">
  <div class="photo" role="img" aria-label="Businesswoman on the phone holding a folder"></div>
  <h2>Recommended Brokers</h2>
  <p>Lorem ipsum dolor sit amet, consectetuer adipiscing elit, sed diam nonummy nibh euismod tincidunt ut laoreet dolore magna aliquam erat volutpat.</p>
  <a class="btn-navy" style="left:437px;top:164px;width:158px;height:42px;line-height:42px">FIND OUT MORE</a>
  <svg class="abs" style="left:1078px;top:80px" width="20" height="26"><path d="M5 3 L15 13 L5 23" stroke="#333" stroke-width="3" fill="none"/></svg>
</section>

<!-- testimonials -->
<h2 class="section-title" style="top:1850px;font-weight:400;font-size:30px">Prople Testimonials</h2>
<p class="abs" style="left:0;top:1896px;width:1200px;text-align:center;font-size:14px;color:#555">Lorem ipsum dolor sit amet, consectetur Donec a consequat mag &nbsp;Aenean eu velit &nbsp;Aenean sollicitudin</p>
<div class="abs" style="left:365px;top:1930px;width:200px;height:1px;background:#ccc"></div>
<div class="abs" style="left:635px;top:1930px;width:200px;height:1px;background:#ccc"></div>
<svg class="abs" style="left:580px;top:1921px" width="54" height="18" aria-hidden="true">
  <g fill="#e2b227"><polygon points="9,1 11,7 17,7 12,11 14,17 9,13 4,17 6,11 1,7 7,7"/><polygon points="27,1 29,7 35,7 30,11 32,17 27,13 22,17 24,11 19,7 25,7"/><polygon points="45,1 47,7 53,7 48,11 50,17 45,13 40,17 42,11 37,7 43,7"/></g>
</svg>
<svg class="abs" style="left:104px;top:1972px" width="20" height="26"><path d="M15 3 L5 13 L15 23" stroke="#333" stroke-width="3" fill="none"/></svg>
<svg class="abs" style="left:1082px;top:1972px" width="20" height="26"><path d="M5 3 L15 13 L5 23" stroke="#333" stroke-width="3" fill="none"/></svg>
<div class="quote"><p><span style="font-size:22px;color:#aaa;position:absolute;left:18px;top:8px">“</span>Lorem sum dolor sit amet, consectetuer adipiscing elit, sed diam nonummy nibh euismod tincidunt ut laoreet re agn aliquam erat volutpat wisi enim ad minim veniam, quis nostrud exerci tation ullamcorper suscipit lobortis nisl ut aliquip modo consequatis autem vel eum iriure dolor in hendrerit in vulputate velit esse molestie consequat, vel illum dolore eu.</p></div>
<div class="quote-photo" role="img" aria-label="Portrait of a smiling client"></div>
<p class="abs" style="left:700px;top:2085px;width:244px;text-align:right;font-style:italic;font-size:12px;color:#222">Ravin, Tallbridge , USA</p>

<!-- footer -->
<footer class="footer">
  <h4 style="left:132px">Quick Links</h4>
  <ul style="left:132px;top:54px"><li>Home</li><li>About Us</li><li>Brokers</li><li>Money Management &amp; Risk</li></ul>
  <ul style="left:255px;top:54px"><li>FAQ</li><li>Register</li><li>Contact Us</li></ul>

  <h4 style="left:375px">Contact Information</h4>
  <svg class="abs" style="left:376px;top:56px" width="12" height="16"><path d="M6 0 C2 0 0 3 0 6 C0 10 6 16 6 16 C6 16 12 10 12 6 C12 3 10 0 6 0 Z" fill="#fff"/><circle cx="6" cy="6" r="2.2" fill="#0c2c4a"/></svg>
  <div class="txt" style="left:402px;top:54px;width:215px">Lorem ipsum dolor consectetuer adipiscing elit, sed diam nonummy bitasa street:395001</div>
  <svg class="abs" style="left:376px;top:118px" width="12" height="14"><path d="M2 1 L5 1 L6 4 L4 6 C5 8 6 9 8 10 L10 8 L13 9 L13 12 C8 13 1 6 2 1 Z" fill="#fff"/></svg>
  <div class="txt" style="left:402px;top:116px">+12 555010204</div>
  <svg class="abs" style="left:376px;top:151px" width="14" height="10"><rect x="0.5" y="0.5" width="13" height="9" fill="none" stroke="#fff"/><path d="M1 1 L7 6 L13 1" stroke="#fff" fill="none"/></svg>
  <div class="txt" style="left:402px;top:147px">info@qlvinstitute.com</div>

  <h4 style="left:652px">Newsletter Sign Up</h4>
  <div class="txt" style="left:652px;top:54px;width:210px;font-size:12px">Lorem ipsudolor sit coec adipiscing elitsite amet</div>
  <div class="email-in">Email Address</div>
  <div class="sub">SUBSCRIBE</div>

  <h4 style="left:912px">Follow Us</h4>
  <span class="soc" style="left:912px"></span>
  <span class="soc" style="left:948px"></span>
  <span class="soc" style="left:984px"></span>
  <span class="soc" style="left:1020px"></span>
  <div class="foot-brand">QLV Institute</div>
</footer>
<div class="copyright">Copyright © 2014 - qlvinstitute.com</div>

</body>
</html>
```